New Business Card Design Project - Moreland Bookkeeping & Tax Services, LLC

Below is a sample image of the card (Fenwick Ledger). I would like to have a designed business card that looks very similar (Front & Back). In addition, I would like to keep the same colors as well. I attached my Business Logo (Moreland Bookkeeping & Tax Services, LLC) that will be on my website.

Target Market(s)

Executives, Business Owners, Board of Directors, Chief Financial Officers

Contact Information for Business Card

Font styles to use
Serif

Colors
0c5ba6
ffffff
5c5c5c

Requirements
Must have
• My Name: Calvin Prewitt, CPA
• Position: Owner
• Phone: (555) 555-0148
• Email: Cprewitt@morelandbooks.com
• Website: www.Morelandbooks.com
• Address: 42917 Birch Hollow Dr #2306
• Harlow Springs, NE 21190
Nice to have
• Same design & color scheme as Fenwick Ledgr Business card sample attached

```html
<!DOCTYPE html>
<html lang="en">
<head>
<meta charset="utf-8">
<title>Moreland Bookkeeping &amp; Tax Services – Business Card</title>
<link rel="stylesheet" href="https://fonts.googleapis.com/css2?family=EB+Garamond:ital,wght@0,400;0,600;1,400&display=swap">
<style>
  :root {
    --brand-blue: #0c5ba6;
    --brand-grey: #5c5c5c;
    --band-grey: #6a7278;
    --white: #ffffff;
    --card-front: #f6f6f6;
    --ink: #1e1e1e;
    --stage: #efefef;
  }
  * { margin: 0; padding: 0; box-sizing: border-box; }
  html, body {
    width: 1200px; height: 757px; overflow: hidden;
    background: var(--stage);
    font-family: "EB Garamond", Georgia, serif;
  }
  .canvas { position: relative; width: 1200px; height: 757px; }

  .card {
    position: absolute; top: 195px;
    width: 498px; height: 299px;
    overflow: hidden;
  }
  .card--front { left: 85px; background: var(--card-front); }
  .card--back { left: 650px; background: var(--brand-blue); }

  /* Front: brand name area */
  .front-brand {
    position: absolute; left: 44px; top: 98px; width: 180px;
    text-align: center; color: var(--brand-blue);
  }
  .front-brand__dot {
    display: block; width: 26px; height: 26px; margin: 0 auto 9px;
    border-radius: 50%; background: var(--brand-blue);
  }
  .front-brand__name {
    font-size: 13px; font-weight: 400; line-height: 16px;
  }

  /* Front: contact block */
  .contact { position: absolute; left: 287px; top: 77px; color: var(--ink); }
  .contact__name {
    font-size: 15.5px; font-weight: 600; color: var(--brand-blue); line-height: 1.1;
  }
  .contact__role { font-size: 10px; font-style: italic; color: #444; margin-top: 1px; }
  .contact__address { font-size: 11px; line-height: 17px; margin-top: 12px; font-style: normal; }
  .contact__list { list-style: none; margin-top: 11px; font-size: 11px; }
  .contact__list li {
    display: flex; align-items: center; gap: 6px; height: 19px; white-space: nowrap;
  }
  .contact__icon { width: 10px; height: 10px; flex: none; }

  .front-bands { position: absolute; left: 0; bottom: 0; width: 498px; height: 26px; }

  /* Back */
  .back-brand {
    position: absolute; left: 0; right: 0; top: 110px;
    text-align: center; color: var(--white);
  }
  .back-brand__dot {
    display: block; width: 40px; height: 40px; margin: 0 auto 42px;
    border-radius: 50%; background: var(--white);
  }
  .back-brand__name {
    font-size: 16.5px; font-weight: 400; letter-spacing: 1.3px;
    text-transform: uppercase; white-space: nowrap;
  }
</style>
</head>
<body>
<main class="canvas">

  <section class="card card--front" aria-label="Business card front">
    <div class="front-brand">
      <span class="front-brand__dot"></span>
      <p class="front-brand__name">Moreland Bookkeeping<br>&amp; Tax Services</p>
    </div>

    <div class="contact">
      <h1 class="contact__name">Calvin Prewitt, CPA</h1>
      <p class="contact__role">Owner</p>
      <address class="contact__address">
        42917 Birch Hollow Dr #2306<br>
        Harlow Springs, NE 21190
      </address>
      <ul class="contact__list">
        <li>
          <svg class="contact__icon" viewBox="0 0 10 10" aria-hidden="true">
            <path fill="#0c5ba6" d="M1 3.2C1 2 2.3 1.5 5 1.5s4 .5 4 1.7v.8H7V3H3v1H1z"/>
            <rect x="2" y="4.3" width="6" height="4.2" rx="1" fill="#0c5ba6"/>
          </svg>
          (555) 555-0148
        </li>
        <li>
          <svg class="contact__icon" viewBox="0 0 10 10" aria-hidden="true">
            <rect x="0.5" y="2" width="9" height="6.5" fill="#0c5ba6"/>
            <path d="M0.8 2.4 5 5.6 9.2 2.4" fill="none" stroke="#fff" stroke-width="0.9"/>
          </svg>
          Cprewitt@morelandbooks.com
        </li>
        <li>
          <svg class="contact__icon" viewBox="0 0 10 10" aria-hidden="true">
            <circle cx="5" cy="5" r="4.6" fill="#0c5ba6"/>
            <path d="M5 .4v9.2M.4 5h9.2" stroke="#fff" stroke-width="0.7"/>
          </svg>
          www.morelandbooks.com
        </li>
      </ul>
    </div>

    <svg class="front-bands" viewBox="0 0 498 26" aria-hidden="true">
      <rect x="0" y="9" width="275" height="17" fill="var(--band-grey)"/>
      <polygon points="262,26 280,0 498,0 498,26" fill="var(--brand-blue)"/>
    </svg>
  </section>

  <section class="card card--back" aria-label="Business card back">
    <div class="back-brand">
      <span class="back-brand__dot"></span>
      <p class="back-brand__name">Moreland Bookkeeping &amp; Tax Services</p>
    </div>
  </section>

</main>
</body>
</html>
```